USB Business Card Design
Pelham Trowbridge Partners Chartered Accountants
Simple
Marcus Trowbridge, CA
Partner
20418-127 Ave
Edmonton, AB
T6K 4M3
T:855.316.2084
P:780.316.2084, D: 780.552.7391
F:780.317.6058
MTrowbridge@ptpca.com
www.ptpca.com
This is going to be printed onto a Business card sized USB stick. They are 2 sided, flashy and plastic coated. This is for extremely high end clients and need to look really amazing! We are open to all ideas, the bosses are partial to a simple look.

```html
<!DOCTYPE html>
<html lang="en">
<head>
<meta charset="utf-8">
<title>Pelham Trowbridge Partners – Business Card</title>
<link href="https://fonts.googleapis.com/css2?family=Open+Sans:wght@400;600;700&display=swap" rel="stylesheet">
<style>
  :root {
    --backdrop: #e4e6ea;
    --card-top: #f7f8fa;
    --card-mid: #e9ecf1;
    --navy: #1c3f8c;
    --navy-deep: #13306f;
    --brand-navy: #1d3d7e;
    --silver-light: #f2f3f5;
    --silver-dark: #b9bdc4;
    --subtitle-grey: #8c9099;
    --white: #ffffff;
    --divider: rgba(255,255,255,0.35);
  }
  * { margin: 0; padding: 0; box-sizing: border-box; }
  html, body {
    width: 1200px; height: 768px; overflow: hidden;
    background: var(--backdrop);
    font-family: "Open Sans", Arial, sans-serif;
  }
  .card {
    position: absolute; left: 100px; top: 98px;
    width: 1000px; height: 572px;
    border-radius: 14px; overflow: hidden;
    background: linear-gradient(180deg, var(--card-top) 0%, var(--card-mid) 52%);
    box-shadow: 0 10px 30px rgba(0,0,0,0.15);
  }
  .brand {
    position: absolute; top: 92px; left: 0; width: 100%;
    text-align: center;
  }
  .brand-name {
    display: inline-flex; align-items: center; gap: 18px;
    font-size: 50px; font-weight: 700; color: var(--brand-navy);
    letter-spacing: 1px;
  }
  .brand-mark {
    width: 40px; height: 40px; border-radius: 50%;
    background: var(--brand-navy);
  }
  .brand-subtitle {
    margin-top: 10px;
    font-size: 17px; font-weight: 600; letter-spacing: 9px;
    color: var(--subtitle-grey); text-transform: uppercase;
  }
  .silver-rule {
    position: absolute; left: 0; width: 100%; height: 10px;
    background: linear-gradient(180deg, var(--silver-light), var(--silver-dark));
  }
  .silver-rule.top { top: 293px; }
  .band {
    position: absolute; top: 303px; left: 0; width: 100%; height: 200px;
    background: linear-gradient(180deg, var(--navy) 0%, var(--navy-deep) 100%);
    color: var(--white);
  }
  .person { position: absolute; left: 70px; top: 36px; }
  .person-name { font-size: 24px; font-weight: 700; }
  .person-title { font-size: 18px; margin-top: 2px; }
  .contact-divider {
    position: absolute; left: 520px; top: 14px; width: 1px; height: 172px;
    background: var(--divider);
  }
  .contact-list {
    position: absolute; left: 540px; top: 12px;
    list-style: none; font-size: 14px; line-height: 22px;
  }
  .contact-list li { display: flex; align-items: center; gap: 10px; }
  .contact-list li.continued { padding-left: 24px; }
  .icon { width: 14px; height: 14px; flex: none; }
  .footer-band {
    position: absolute; top: 503px; left: 0; width: 100%; height: 69px;
    background: linear-gradient(180deg, var(--silver-dark) 0%, var(--silver-light) 40%, #d6d9de 100%);
  }
</style>
</head>
<body>
  <div class="card">
    <div class="brand">
      <div class="brand-name"><span class="brand-mark"></span>Pelham Trowbridge Partners</div>
      <div class="brand-subtitle">Chartered Accountants</div>
    </div>

    <div class="silver-rule top"></div>

    <div class="band">
      <div class="person">
        <div class="person-name">Marcus Trowbridge, CA</div>
        <div class="person-title">Partner</div>
      </div>

      <div class="contact-divider"></div>

      <ul class="contact-list">
        <li><svg class="icon" viewBox="0 0 14 14"><path d="M7 1a4 4 0 0 0-4 4c0 3 4 8 4 8s4-5 4-8a4 4 0 0 0-4-4z" fill="#fff"/><circle cx="7" cy="5" r="1.5" fill="#1c3f8c"/></svg>20418-127 Ave</li>
        <li class="continued">Edmonton, AB T6K 4M3</li>
        <li><svg class="icon" viewBox="0 0 14 14"><path d="M3 1.5l2 .3 1 3-1.3 1a7 7 0 0 0 3.5 3.5l1-1.3 3 1 .3 2-1.5 1.5C6 12 2 8 1.5 3z" fill="#fff"/></svg>855.316.2084</li>
        <li><svg class="icon" viewBox="0 0 14 14"><path d="M3 1.5l2 .3 1 3-1.3 1a7 7 0 0 0 3.5 3.5l1-1.3 3 1 .3 2-1.5 1.5C6 12 2 8 1.5 3z" fill="#fff"/></svg>780.316.2084</li>
        <li><svg class="icon" viewBox="0 0 14 14"><rect x="4" y="1" width="6" height="12" rx="1.2" fill="#fff"/><rect x="5" y="2.5" width="4" height="7" fill="#1c3f8c"/></svg>D: 780.552.7391</li>
        <li><svg class="icon" viewBox="0 0 14 14"><rect x="1.5" y="5" width="11" height="6" rx="1" fill="#fff"/><rect x="4" y="1.5" width="6" height="3" fill="#fff"/><rect x="4" y="9" width="6" height="3.5" fill="#fff" stroke="#1c3f8c" stroke-width="0.8"/></svg>780.317.6058</li>
        <li><svg class="icon" viewBox="0 0 14 14"><rect x="1" y="3" width="12" height="8" rx="1" fill="#fff"/><path d="M1.5 3.5L7 8l5.5-4.5" fill="none" stroke="#1c3f8c" stroke-width="1"/></svg>MTrowbridge@ptpca.com</li>
        <li><svg class="icon" viewBox="0 0 14 14"><circle cx="7" cy="7" r="5.5" fill="none" stroke="#fff" stroke-width="1.3"/><path d="M1.5 7h11M7 1.5c-3 3-3 8 0 11M7 1.5c3 3 3 8 0 11" fill="none" stroke="#fff" stroke-width="1"/></svg>www.ptpca.com</li>
      </ul>
    </div>

    <div class="footer-band"></div>
  </div>
</body>
</html>
```